hop3PeakTrail

I have a weebly web site need design and formatted using the color and look and feel similar to another site. Our web site is currently behind password. http://www.hop3peaktrail.com pwd Blue7RiverLamp!

I'm looking to layout like https://www.kravlinpartners.com/blog

We want a yellow, light yellow, gray and black as the main colors. Attached image show color of yellow and light yellow. I don't have a specific color for gray and black. If you think there should be addition colors in the color pallet we greatly appreciate your expertise.

We need the logo designed. Right now its just text.

I don't like that our site list the full blog one after another, I like the tiled look, image, tile and small amount of text. Click and go into a blog. Often at the end of a blog you can jump back to main page, and/or see three additional blog tiles. We like how orange carries through on buttons and text, Accent colors are consistent.

I need CSS that can be inserted into each form. If you look at the source of the form, you can see how I tried to format given the form elements. I cannot change the form, but I can easily insert CSS for the form.

I need a template that can be used in Weebly site either you edit on our site or give us a template that can be used.

Industry/Entity Type

Life Coaching

Coding

Coded - Design and coding required

Number of Pages Required

5+ page

Font styles to use
Sans Serif

Requirements
Must have
• What to build a clean color pallet using the Yellow, light yellow I uploaded image. Also a gray and black.

```html
<!DOCTYPE html>
<html lang="en">
<head>
<meta charset="utf-8">
<title>hop3PeakTrail – Blog</title>
<link href="https://fonts.googleapis.com/css2?family=Roboto:wght@400;500;700;900&family=Open+Sans:wght@400;600;700&family=Inter:wght@300;400&display=swap" rel="stylesheet">
<style>
:root{
  --yellow:#fbb20f;
  --yellow-soft:#fcd46a;
  --cream:#fde8c8;
  --red:#e8342c;
  --ink:#111111;
  --text:#333333;
  --gray:#666666;
  --line:#e4e4e4;
  --white:#ffffff;
}
*{margin:0;padding:0;box-sizing:border-box}
html,body{width:1200px;height:2751px;overflow:hidden;background:var(--white)}
body{font-family:"Roboto",sans-serif;color:var(--text);position:relative}
a{color:inherit;text-decoration:none}

.site-header{height:65px;display:flex;align-items:center;justify-content:space-between;padding:0 109px 0 113px}
.brand{font-family:"Roboto",sans-serif;font-weight:700;font-size:23px;color:var(--ink)}
.main-nav{display:flex;gap:38px;font-family:"Open Sans",sans-serif;font-weight:600;font-size:16.5px;color:var(--ink)}
.main-nav .active{color:var(--red)}

.hero{position:relative;height:554px;background:linear-gradient(180deg,#d7b8ad 0%,#c6a7a0 20%,#8a98ad 45%,#4e6583 65%,#3a4a58 82%,#2c3136 100%);text-align:center}
.hero::before{content:"";position:absolute;inset:0;background:linear-gradient(90deg,rgba(40,40,45,.75) 0%,rgba(0,0,0,0) 30%,rgba(0,0,0,0) 70%,rgba(60,60,50,.75) 100%)}
.hero-content{position:relative;padding-top:124px}
.hero h1{font-family:"Roboto",sans-serif;font-weight:700;font-size:63px;color:var(--ink);letter-spacing:.5px;line-height:1}
.hero p{font-family:"Open Sans",sans-serif;font-weight:600;font-size:19px;color:var(--white);margin-top:14px}
.btn{display:inline-flex;align-items:center;justify-content:center;background:var(--yellow);color:var(--ink);font-family:"Open Sans",sans-serif;font-weight:700;border-radius:3px}
.hero .btn{width:201px;height:51px;font-size:17px;margin-top:14px}

.latest{padding-top:55px}
.section-title{text-align:center;font-weight:700;font-size:40px;color:var(--ink);line-height:1.1}
.section-title::after{content:"";display:block;width:79px;height:3px;background:var(--yellow);margin:12px auto 0}
.filter-bar{margin-top:22px;height:87px;border-top:1px solid var(--line);border-bottom:1px solid var(--line);display:flex;align-items:center;padding:0 113px;position:relative}
.tabs{display:flex;font-family:"Open Sans",sans-serif;font-weight:600;font-size:17.5px;color:var(--ink)}
.tabs span{margin-right:63px;position:relative}
.tabs .active{color:var(--red)}
.tabs .active::after{content:"";position:absolute;left:-6px;right:-6px;top:52px;height:2px;background:var(--red)}
.search{position:absolute;left:675px;top:20px;width:412px;height:46px;border:1px solid #cfcfcf;display:flex}
.search span{flex:1;padding-left:16px;line-height:44px;font-size:15px;color:#555}
.search .btn{width:108px;height:40px;margin:2px;font-size:17px;border-radius:0}

.card-grid{display:grid;grid-template-columns:repeat(3,301px);column-gap:37px;row-gap:39px;padding:43px 0 0 112px}
.card{height:406px;border:1px solid var(--line);display:flex;flex-direction:column}
.card-media{height:210px;position:relative;flex:none}
.tag{position:absolute;left:0;bottom:0;background:var(--yellow);color:var(--ink);font-weight:500;font-size:14px;padding:5px 14px 3px 12px;border-radius:0 14px 0 0}
.card h3{font-weight:700;font-size:21px;line-height:25px;color:var(--ink);padding:13px 7px 0}
.card p{font-family:"Inter",sans-serif;font-weight:300;font-size:14px;letter-spacing:-0.25px;line-height:25.6px;color:#333;padding:5px 7px 0;display:-webkit-box;-webkit-line-clamp:4;-webkit-box-orient:vertical;overflow:hidden}
.card-meta{margin-top:auto;height:34px;flex:none;border-top:1px solid var(--line);display:flex;font-family:"Open Sans",sans-serif;font-size:14.5px;color:var(--ink)}
.card-meta span{display:flex;align-items:center;gap:5px;padding:0 9px;border-right:1px solid var(--line)}
.card-meta span:last-child{border-right:none;padding-left:14px}
.card-meta svg{width:13px;height:13px}

.pager{display:flex;justify-content:center;align-items:center;gap:6px;margin-top:47px;height:34px}
.pager b{width:34px;height:34px;display:flex;align-items:center;justify-content:center;background:var(--yellow-soft);font-weight:500;font-size:17px;color:var(--ink);border-radius:2px}
.pager b.on{background:var(--yellow)}
.pager svg{width:20px;height:20px;margin:0 8px}

.about{position:absolute;top:1938px;left:0;width:1200px;height:455px;display:flex}
.about-media{width:601px;background:linear-gradient(180deg,#a89c8e 0%,#6c5f52 45%,#3c302a 100%)}
.about-body{flex:1;background:var(--cream);padding:72px 0 0 34px}
.about-body h2{font-weight:700;font-size:40px;color:var(--ink)}
.about-body h2::after{content:"";display:block;width:68px;height:3px;background:var(--yellow);margin-top:10px}
.about-body p{font-family:"Inter",sans-serif;font-weight:300;font-size:16px;letter-spacing:-0.3px;line-height:30px;color:var(--ink);margin-top:20px;width:450px}
.about-body .btn{width:171px;height:51px;font-size:17px;margin-top:24px}

.site-footer{position:absolute;top:2393px;left:0;width:1200px;height:358px;background:var(--ink);color:var(--white)}
.footer-brand{position:absolute;left:126px;top:62px;font-weight:700;font-size:36px}
.social{position:absolute;left:161px;top:131px;display:flex;gap:5px}
.social i{width:32px;height:32px;border-radius:50%;background:var(--white);display:block}
.footer-col{position:absolute;top:66px;font-family:"Inter",sans-serif;font-weight:300;font-size:14px;letter-spacing:-0.2px}
.footer-col h4{font-family:"Roboto",sans-serif;font-weight:700;font-size:17px;letter-spacing:0;margin-bottom:8px}
.footer-col li{list-style:none;line-height:28px}
.links{left:454px}
.newsletter{left:710px}
.newsletter p{line-height:28px;width:360px}
.email{margin:16px 0 0 6px;width:371px;height:47px;background:var(--white);color:#333;font-size:14px;line-height:47px;padding-left:19px}
.newsletter .btn{margin:13px 0 0 6px;width:173px;height:47px;font-size:17px;border-radius:0;letter-spacing:0}
.copyright{position:absolute;left:0;right:0;top:315px;text-align:center;font-family:"Inter",sans-serif;font-weight:300;font-size:15px}
</style>
</head>
<body>
<header class="site-header">
  <div class="brand">hop3PeakTrail</div>
  <nav class="main-nav">
    <a class="active">BLOG</a><a>WHO WE ARE</a><a>OUR MODEL</a><a>WHO USES HOP3PEAKTRAIL</a><a>PRICING</a>
  </nav>
</header>

<section class="hero" role="img" aria-label="Hiker standing on a rocky summit between cliffs, overlooking mountain valleys at dusk">
  <div class="hero-content">
    <h1>FINDING JOY IN CHAOS</h1>
    <p>Let us help you find a path</p>
    <a class="btn">SUBSCRIBE NOW</a>
  </div>
</section>

<section class="latest">
  <h2 class="section-title">LATEST BLOG</h2>
  <div class="filter-bar">
    <div class="tabs"><span class="active">All</span><span>Career</span><span>Finance</span><span>Health</span><span>Tool</span></div>
    <div class="search"><span>Search here...</span><a class="btn">SEARCH</a></div>
  </div>

  <div class="card-grid">
    <article class="card">
      <div class="card-media" role="img" aria-label="Woman laughing at her office desk with a laptop" style="background:linear-gradient(135deg,#6b5a4e,#c9a898 55%,#d8cfc7)"><span class="tag">HEALTH</span></div>
      <h3>Improvisation</h3>
      <p>Essential to living a joyful life is the ability to adapt to any situation. Life is always going to throw curveballs, and we’re always going to need to find a different way...</p>
      <div class="card-meta"><span><svg viewBox="0 0 14 14"><rect x="1" y="2.5" width="12" height="10.5" fill="none" stroke="#111" stroke-width="1.4"/><path d="M1 5.5h12M4 1v3M10 1v3" stroke="#111" stroke-width="1.4"/></svg>January 18,2020</span><span><svg viewBox="0 0 14 14"><path d="M1 7c2-3.5 10-3.5 12 0c-2 3.5-10 3.5-12 0z" fill="#111"/><circle cx="7" cy="7" r="1.8" fill="#fff"/></svg>232</span><span><svg viewBox="0 0 14 14"><path d="M9 2l4 3.5L9 9V7C6 7 4 8 3 10c0-4 2-6 6-6.5z" fill="none" stroke="#111" stroke-width="1.3"/><path d="M6 3H1v10h10v-3" fill="none" stroke="#111" stroke-width="1.3"/></svg>Share</span></div>
    </article>
    <article class="card">
      <div class="card-media" role="img" aria-label="Climber resting on a rocky peak under a blue sky" style="background:linear-gradient(180deg,#2f5da8,#7fa6d8 45%,#8d8a86 75%,#4b4a48)"><span class="tag">HEALTH</span></div>
      <h3>Climbing a Mountain</h3>
      <p>At hop3PeakTrail we focus on your career, health, and finances to help you improve your overall well being. Today I’m going to focus on health.</p>
      <div class="card-meta"><span><svg viewBox="0 0 14 14"><rect x="1" y="2.5" width="12" height="10.5" fill="none" stroke="#111" stroke-width="1.4"/><path d="M1 5.5h12M4 1v3M10 1v3" stroke="#111" stroke-width="1.4"/></svg>January 18,2020</span><span><svg viewBox="0 0 14 14"><path d="M1 7c2-3.5 10-3.5 12 0c-2 3.5-10 3.5-12 0z" fill="#111"/><circle cx="7" cy="7" r="1.8" fill="#fff"/></svg>232</span><span><svg viewBox="0 0 14 14"><path d="M9 2l4 3.5L9 9V7C6 7 4 8 3 10c0-4 2-6 6-6.5z" fill="none" stroke="#111" stroke-width="1.3"/><path d="M6 3H1v10h10v-3" fill="none" stroke="#111" stroke-width="1.3"/></svg>Share</span></div>
    </article>
    <article class="card">
      <div class="card-media" role="img" aria-label="Person sitting by a window looking at a phone" style="background:linear-gradient(90deg,#3a2f2a,#c7b3a3 35%,#8f7a6c 60%,#1e1e22)"><span class="tag">TOOL</span></div>
      <h3>1% Should Scare You</h3>
      <p>At hop3PeakTrail, we focus on 3 areas of your life in which we can help you achieve a higher well being: career, heath, and finances. Today, let’s focus</p>
      <div class="card-meta"><span><svg viewBox="0 0 14 14"><rect x="1" y="2.5" width="12" height="10.5" fill="none" stroke="#111" stroke-width="1.4"/><path d="M1 5.5h12M4 1v3M10 1v3" stroke="#111" stroke-width="1.4"/></svg>January 18,2020</span><span><svg viewBox="0 0 14 14"><path d="M1 7c2-3.5 10-3.5 12 0c-2 3.5-10 3.5-12 0z" fill="#111"/><circle cx="7" cy="7" r="1.8" fill="#fff"/></svg>232</span><span><svg viewBox="0 0 14 14"><path d="M9 2l4 3.5L9 9V7C6 7 4 8 3 10c0-4 2-6 6-6.5z" fill="none" stroke="#111" stroke-width="1.3"/><path d="M6 3H1v10h10v-3" fill="none" stroke="#111" stroke-width="1.3"/></svg>Share</span></div>
    </article>
    <article class="card">
      <div class="card-media" role="img" aria-label="Man meditating cross-legged in a modern office lobby" style="background:linear-gradient(135deg,#3b3a38,#8a7a66 45%,#c9b79c 80%,#e6dccb)"><span class="tag">CARRER</span></div>
      <h3>Focus</h3>
      <p>Recently, I was reading an article on attention management when I interrupted myself to text a friend. I had to laugh at my own absurdity -- I clearly need</p>
      <div class="card-meta"><span><svg viewBox="0 0 14 14"><rect x="1" y="2.5" width="12" height="10.5" fill="none" stroke="#111" stroke-width="1.4"/><path d="M1 5.5h12M4 1v3M10 1v3" stroke="#111" stroke-width="1.4"/></svg>January 18,2020</span><span><svg viewBox="0 0 14 14"><path d="M1 7c2-3.5 10-3.5 12 0c-2 3.5-10 3.5-12 0z" fill="#111"/><circle cx="7" cy="7" r="1.8" fill="#fff"/></svg>232</span><span><svg viewBox="0 0 14 14"><path d="M9 2l4 3.5L9 9V7C6 7 4 8 3 10c0-4 2-6 6-6.5z" fill="none" stroke="#111" stroke-width="1.3"/><path d="M6 3H1v10h10v-3" fill="none" stroke="#111" stroke-width="1.3"/></svg>Share</span></div>
    </article>
    <article class="card">
      <div class="card-media" role="img" aria-label="Two coworkers celebrating at a laptop in an office" style="background:linear-gradient(135deg,#c8d2d3,#6f7f82 45%,#b7aea4 75%,#5b4b40)"><span class="tag">FINANCE</span></div>
      <h3>Mutual Purpose</h3>
      <p>Often in both our personal and professional life, we need to have hard conversations. These talks come in many forms. Maybe a friend has said something hurtful, or</p>
      <div class="card-meta"><span><svg viewBox="0 0 14 14"><rect x="1" y="2.5" width="12" height="10.5" fill="none" stroke="#111" stroke-width="1.4"/><path d="M1 5.5h12M4 1v3M10 1v3" stroke="#111" stroke-width="1.4"/></svg>January 18,2020</span><span><svg viewBox="0 0 14 14"><path d="M1 7c2-3.5 10-3.5 12 0c-2 3.5-10 3.5-12 0z" fill="#111"/><circle cx="7" cy="7" r="1.8" fill="#fff"/></svg>232</span><span><svg viewBox="0 0 14 14"><path d="M9 2l4 3.5L9 9V7C6 7 4 8 3 10c0-4 2-6 6-6.5z" fill="none" stroke="#111" stroke-width="1.3"/><path d="M6 3H1v10h10v-3" fill="none" stroke="#111" stroke-width="1.3"/></svg>Share</span></div>
    </article>
    <article class="card">
      <div class="card-media" role="img" aria-label="Open book with pages folded into a heart at sunset" style="background:linear-gradient(180deg,#e9a07c,#d86f6a 45%,#7a3246 75%,#2e1a22)"><span class="tag">HEALTH</span></div>
      <h3>Love</h3>
      <p>As a culture, we’re pretty bad at teaching love. I bet you learned math in school, how to ride a bike, maybe how to play a musical instrument. But when were you taught</p>
      <div class="card-meta"><span><svg viewBox="0 0 14 14"><rect x="1" y="2.5" width="12" height="10.5" fill="none" stroke="#111" stroke-width="1.4"/><path d="M1 5.5h12M4 1v3M10 1v3" stroke="#111" stroke-width="1.4"/></svg>January 18,2020</span><span><svg viewBox="0 0 14 14"><path d="M1 7c2-3.5 10-3.5 12 0c-2 3.5-10 3.5-12 0z" fill="#111"/><circle cx="7" cy="7" r="1.8" fill="#fff"/></svg>232</span><span><svg viewBox="0 0 14 14"><path d="M9 2l4 3.5L9 9V7C6 7 4 8 3 10c0-4 2-6 6-6.5z" fill="none" stroke="#111" stroke-width="1.3"/><path d="M6 3H1v10h10v-3" fill="none" stroke="#111" stroke-width="1.3"/></svg>Share</span></div>
    </article>
  </div>

  <nav class="pager">
    <svg viewBox="0 0 20 20"><path d="M13 3L6 10l7 7" fill="none" stroke="#333" stroke-width="1.5"/></svg>
    <b class="on">1</b><b>2</b><b>3</b>
    <svg viewBox="0 0 20 20"><path d="M7 3l7 7-7 7" fill="none" stroke="#333" stroke-width="1.5"/></svg>
  </nav>
</section>

<section class="about">
  <div class="about-media" role="img" aria-label="Group sitting cross-legged on a wooden floor in a bright loft studio"></div>
  <div class="about-body">
    <h2>WHO WE ARE</h2>
    <p>We started hop3PeakTrail with a passion to help people navigate the multitude of decisions in life and develop a process to create stronger wellbeing.&nbsp; We believe that in order to achieve purpose and fulfillment,&nbsp; you need to focus on your health (physical and mental), career, and finances.</p>
    <a class="btn">LEARN MORE</a>
  </div>
</section>

<footer class="site-footer">
  <div class="footer-brand">hop3PeakTrail</div>
  <div class="social" aria-label="Social links"><i></i><i></i><i></i><i></i></div>
  <div class="footer-col links">
    <h4>QUICK LINKS</h4>
    <ul><li>Blog</li><li>Who We Are</li><li>Our Model</li><li>Who Uses Hop3peaktrail</li><li>Pricing</li><li>Subscribe Now</li></ul>
  </div>
  <div class="footer-col newsletter">
    <h4>SUBSCRIBE TO OUR NEWSLETTER</h4>
    <p>"Lorem ipsum dolor sit amet, consectetur adipiscing elit, sed do eiusmod tempor incididunt ut labore et</p>
    <div class="email">Email Address</div>
    <a class="btn">SUBSCRIBE NOW</a>
  </div>
  <div class="copyright">© 2021hop3peaktrail. All Rights Reserved.</div>
</footer>
</body>
</html>
```